Poster to promote Global Critter Care Fest

Hi Designers,

Animal lovers all over the world are grateful for the work of vets.

To recognize all their efforts, Global Critter Care Fest takes place globally on April 30. This year's theme is 'Continuing education with a one health focus'.

It's about working alongside the human health sector to tackle animal disease and food safety. Read more here: http://www.brenvalu.org/for-the-media/press-releases/detail/article/global-critter-care-fest-award-2016/

We want you to design a poster to promote the day, and the key message.

The poster must feature:
- the words 'Global Critter Care Fest'
- the date 'April 30, 2016'
- the theme 'Continuing education with a one health focus

You can choose any imagery and colors you feel will be engaging for the audience and will reflect the industry and messages.

Think animal, vets, pets, caring, health.

Looking forward to seeing your ideas.

Thanks

PixelHive

• - the words 'Global Critter Care Fest'
• - the date 'April 30, 2016'
• - the theme 'Continuing education with a one health focus

```html
<!DOCTYPE html>
<html lang="en">
<head>
<meta charset="utf-8">
<title>Global Critter Care Fest — Poster</title>
<link rel="stylesheet" href="https://fonts.googleapis.com/css2?family=Roboto+Condensed:wght@300;700&family=Courier+Prime&display=swap">
<style>
  :root {
    --backdrop: #e4e3e1;
    --magenta-deep: #c0114f;
    --magenta-bright: #ea175f;
    --paper: #eeeeee;
    --ink-light: #f3f3f3;
    --rule: rgba(255, 255, 255, 0.55);
  }
  html, body {
    margin: 0;
    padding: 0;
    width: 1200px;
    height: 1000px;
    overflow: hidden;
    background: var(--backdrop);
  }
  .canvas {
    position: relative;
    width: 1200px;
    height: 1000px;
  }
  .poster {
    position: absolute;
    left: 320px;
    top: 50px;
    width: 560px;
    height: 900px;
    overflow: hidden;
    background: linear-gradient(175deg, var(--magenta-deep) 0%, var(--magenta-deep) 55%, var(--magenta-bright) 100%);
    box-shadow: 0 10px 30px rgba(0, 0, 0, 0.18);
  }
  .poster__split {
    position: absolute;
    inset: 0;
    width: 100%;
    height: 100%;
  }
  .poster__critter {
    position: absolute;
    left: 530px;
    top: 548px;
    width: 14px;
    height: 24px;
    border-radius: 7px 7px 2px 2px;
    background: var(--magenta-deep);
  }
  .headline {
    position: absolute;
    right: 28px;
    top: 590px;
    margin: 0;
    text-align: right;
    color: var(--ink-light);
    font-family: "Roboto Condensed", sans-serif;
    line-height: 1;
  }
  .headline__date {
    font-weight: 300;
    font-size: 30px;
  }
  .headline__thin {
    font-weight: 300;
    font-size: 44px;
    letter-spacing: 1px;
  }
  .headline__bold {
    display: block;
    margin-top: 4px;
    font-weight: 700;
    font-size: 50px;
    letter-spacing: 0.5px;
  }
  .divider {
    position: absolute;
    left: 40px;
    right: 28px;
    top: 706px;
    border-top: 1px dashed var(--rule);
  }
  .theme {
    position: absolute;
    right: 28px;
    top: 728px;
    margin: 0;
    text-align: right;
    color: var(--ink-light);
    font-family: "Courier Prime", monospace;
    font-size: 17px;
    letter-spacing: 1.2px;
    line-height: 1.35;
  }
</style>
</head>
<body>
<main class="canvas">
  <article class="poster">
    <svg class="poster__split" viewBox="0 0 560 900" aria-hidden="true">
      <polygon points="145,0 560,0 560,598" fill="var(--paper)"/>
    </svg>
    <div class="poster__critter" role="img" aria-label="Small cat silhouette sitting on the diagonal edge"></div>
    <h1 class="headline">
      <span class="headline__date">April 30, 2016</span>
      <span class="headline__thin">GLOBAL</span>
      <span class="headline__bold">CRITTER CARE FEST</span>
    </h1>
    <div class="divider"></div>
    <p class="theme">Continuing education<br>with a one health focus</p>
  </article>
</main>
</body>
</html>
```